Modern Verco Brokers Business Card design

We are a relatively new real estate agency. We need a business card that reflects the professionalism and prestige of our company but is also modern and fresh, based around our logo.
We would love to utilise Verco Brokers.
Happy to let the designers use their imagination and see what they come up with (we're not very creative, so have no ideas for you, sorry) :-)
We'd like one for each staff member, but I've just provided one staff members photo here to avoid confusion.

Target Market(s)

Families

Industry/Entity Type

Real Estate Agent

Contact Information for Business Card

Dale Verco - Director & Principal
Mobile: 0491 627 540
Email: dale.verco@vbrokers.example.au
Phone: (08) 8374 6150
Fax: (08) 8374 6198
www.vercobrokersproperty.example.au

Font styles to use
Other font styles liked:
• Kabel Dm BT

Requirements
Must have
• Contact details, logo, photo, Verco Brokers
Nice to have
• Modern interesting features that will make people comment. Nothing too feminine nor too masculine.
Should not have
• No houses! Nothing typical of a real estate agent.

```html
<!DOCTYPE html>
<html lang="en">
<head>
<meta charset="utf-8">
<title>Dale Verco – Business Card</title>
<link rel="stylesheet" href="https://fonts.googleapis.com/css2?family=Lexend:wght@400;500;600&display=swap">
<style>
  :root {
    --navy: #1b3f78;
    --navy-light: #8e9ab8;
    --gold: #d2ad6a;
    --gold-dark: #9a7634;
    --gold-text: #c9a15a;
    --brand: #a5865a;
    --ink: #1d1d1d;
    --paper: #ffffff;
    --photo-dark: #2a2a2c;
  }
  html, body { margin: 0; padding: 0; overflow: hidden; background: var(--paper); }
  .card {
    position: relative;
    width: 1200px;
    height: 692px;
    overflow: hidden;
    background: var(--paper);
    font-family: "Lexend", sans-serif;
  }
  .card-shapes { position: absolute; inset: 0; }
  .contact-list {
    position: absolute;
    left: 46px;
    top: 28px;
    margin: 0;
    padding: 0;
    list-style: none;
  }
  .contact-item {
    display: flex;
    align-items: center;
    height: 78px;
    font-size: 42px;
    font-weight: 600;
    color: var(--gold-text);
    text-shadow: 3px 3px 3px rgba(0, 0, 0, 0.55);
    letter-spacing: 0.5px;
  }
  .contact-item svg { width: 36px; height: 40px; margin-right: 12px; flex: none; }
  .brand-name {
    position: absolute;
    left: 110px;
    top: 350px;
    margin: 0;
    font-size: 74px;
    font-weight: 500;
    line-height: 96px;
    color: var(--brand);
  }
  .staff-name {
    position: absolute;
    left: 540px;
    right: 0;
    top: 448px;
    margin: 0;
    text-align: center;
    font-size: 41px;
    font-weight: 500;
    color: var(--ink);
  }
  .staff-role {
    position: absolute;
    left: 626px;
    top: 526px;
    margin: 0;
    font-size: 41px;
    font-weight: 600;
    color: var(--ink);
  }
  .web-list {
    position: absolute;
    left: 628px;
    top: 596px;
    margin: 0;
    padding: 0;
    list-style: none;
    font-size: 21px;
    font-weight: 400;
    line-height: 34px;
    color: var(--ink);
  }
</style>
</head>
<body>
<div class="card">
  <svg class="card-shapes" width="1200" height="692" viewBox="0 0 1200 692">
    <defs>
      <radialGradient id="navyGlow" cx="0" cy="0" r="1.1">
        <stop offset="0" stop-color="var(--navy-light)"/>
        <stop offset="0.45" stop-color="#3c5a8e"/>
        <stop offset="1" stop-color="var(--navy)"/>
      </radialGradient>
      <linearGradient id="photoTone" x1="0" y1="0" x2="0" y2="1">
        <stop offset="0" stop-color="#3a3a3c"/>
        <stop offset="0.5" stop-color="#6a6e74"/>
        <stop offset="1" stop-color="var(--photo-dark)"/>
      </linearGradient>
    </defs>
    <polygon class="blue-panel" points="0,0 858,0 543,692 0,692" fill="url(#navyGlow)"/>
    <polygon class="name-band" points="492,430 1200,430 1200,525 492,525" fill="var(--gold)"/>
    <polygon class="band-fold" points="492,525 625,525 583,606" fill="var(--gold-dark)"/>
    <ellipse class="staff-photo" role="img" aria-label="Portrait photo of Dale Verco in a dark suit" cx="961" cy="212" rx="128" ry="196" fill="url(#photoTone)"/>
  </svg>

  <ul class="contact-list">
    <li class="contact-item">
      <svg viewBox="0 0 36 40" aria-label="Mobile"><rect x="8" y="2" width="20" height="36" rx="3" fill="#222" stroke="#ddd" stroke-width="1.5"/><rect x="11" y="6" width="14" height="12" fill="#9aa"/><g fill="#ccc"><rect x="11" y="22" width="4" height="3"/><rect x="16" y="22" width="4" height="3"/><rect x="21" y="22" width="4" height="3"/><rect x="11" y="27" width="4" height="3"/><rect x="16" y="27" width="4" height="3"/><rect x="21" y="27" width="4" height="3"/></g></svg>
      <span>0491 627 540</span>
    </li>
    <li class="contact-item">
      <svg viewBox="0 0 36 40" aria-label="Phone"><path d="M4 16 Q18 4 32 16 L28 20 L24 16 L12 16 L8 20 Z" fill="#222" stroke="#eee" stroke-width="1.5"/><path d="M10 20 L26 20 L31 32 L5 32 Z" fill="#222" stroke="#eee" stroke-width="1.5"/><circle cx="18" cy="26" r="4" fill="none" stroke="#eee" stroke-width="1.5"/></svg>
      <span>(08) 8374 6150</span>
    </li>
    <li class="contact-item">
      <svg viewBox="0 0 36 40" aria-label="Fax"><rect x="4" y="14" width="28" height="20" rx="2" fill="#222" stroke="#eee" stroke-width="1.5"/><rect x="10" y="6" width="16" height="10" fill="#eee" stroke="#222"/><g fill="#eee"><rect x="15" y="20" width="4" height="3"/><rect x="21" y="20" width="4" height="3"/><rect x="15" y="26" width="4" height="3"/><rect x="21" y="26" width="4" height="3"/></g><rect x="7" y="18" width="5" height="13" fill="#888"/></svg>
      <span>(08) 8374 6198</span>
    </li>
  </ul>

  <p class="brand-name">Verco<br>Brokers</p>

  <h1 class="staff-name">Dale Verco</h1>
  <p class="staff-role">Director &amp; Principal</p>

  <ul class="web-list">
    <li>dale.verco@vbrokers.example.au</li>
    <li>www.vercobrokersproperty.example.au</li>
  </ul>
</div>
</body>
</html>
```